practical mindfulness guide needs a book cover, back and front

I require a book cover for a print and eBook. Both front and back. The title of the book is: Returning to Stillness:
Refreshing Your Routine to Ease Worry, Grow Inner Awareness, and Open Your Boundless Promise.
Sales Handle
Eight weeks is good, fifty-two is better: this warm, personal guide will help you deepen in mindfulness across the year, weaving it into all aspects of your life.

Back cover
Returning to Stillness offers an evidence-based, step-by-step journey through a year of personal change. Drawing on his path of overcoming dyslexia, autism, trauma, and anxiety, Dr. Martin Olund blends mindfulness, psychology, and holistic healing in this accessible guide to lasting personal transformation.

Unlike short-term programs, this book offers a full year of structured, practical exercises—scientifically grounded and deeply personal—to help you turn mindfulness into a lifelong habit. Each week, you'll explore simple yet profound practices to manage stress, build emotional resilience, and reconnect with your deeper wisdom. Through guided meditations, reflections, and trainings, you’ll rewire old patterns and learn to embrace the present moment with clarity and compassion. Whether you're seeking relief from chronic stress, clarity in uncertain times, or a deeper connection to yourself and your life, Gentle Renewal will meet you where you are. It’s not about perfection—it’s about learning to show up, fully present, for the beauty and messiness of life.

Bio
Martin Olund is a mindfulness and Dharma teacher, award-winning author, and former professor of social work with over 40 years of contemplative practice. He teaches insight meditation and has worked extensively with diverse communities, including unhoused populations, combat veterans with PTSD, and First Nations groups, blending mindfulness with deep cultural respect. Martin holds a PhD in social work and has authored several mindfulness and social justice books. He teaches with Quiet Harbor Sangha (QHS) and founded the Cedarline Stillness Sitting Circle. His teaching invites a return to presence, clarity, and compassionate action.

I like the simple design of the book Awareness: The Quiet Secret Within Breathing and Living Fully in Your Days. But something more eye-catching would be welcome. It is a book for someone who has taken an intro mindfulness course and wants to get back into it, hence the "coming back" in the title. AI suggested things like a calendar with "practice" written on one day, with it crossed out. At any rate, it would be nice to illustrate this idea of coming back or renewing mindfulness practice with a 52-week practice guide. The book is basically 52 topics with an intro, reflections, practices, and encouragement.

Target Market(s)

Someone who has completed a short introductory mindfulness program like MBSR or MBCT and aims to cultivate a consistent, sustainable meditation and mindfulness practice. Eight weeks is a great start, but it simply isn’t enough time to firmly establish the habits of mindfulness, much less to delve into the layers of somatic and emotional nuance that it can offer. People require varying support levels. For example, those with chronic depression may need intensive follow-ups, while others might benefit from occasional refreshers. This book offers a flexible approach that readers can tailor to their own needs. The secondary target audience includes individuals who had a previous meditation practice but have let it lapse and wish to revitalize it. Through positive reviews, press, social media, and word-of-mouth, I also hope to attract other types of readers, such as those experiencing high stress or anxiety, individuals navigating major life transitions, professionals like therapists, counselors, and coaches, people seeking to develop resiliency or emotional intelligence, and those curious about integrating spiritual wisdom into everyday life.

Industry/Entity Type

Self help

Colors
0054AA
0677BA
7BADD7
CADEEF
E8F1F8

Requirements
Must have
• The title and my name as Martin J. Olund. Provided logo on bottom of back cover
Nice to have
• Something that says this book is for those coming back to practice. some tie in with my Youtube channel at https://www.videoplace.example/@martinsits
Should not have
• Buddhas or other religious symbols

```html
<!DOCTYPE html>
<html lang="en">
<head>
<meta charset="utf-8">
<title>Returning to Stillness – Book Cover</title>
<link rel="stylesheet" href="https://fonts.googleapis.com/css2?family=Bebas+Neue&family=Oswald:wght@400;700&family=Montserrat:wght@400&family=Jost:wght@400&display=swap">
<style>
  :root {
    --cover-blue: #80a9d9;
    --navy: #25215e;
    --white: #ffffff;
    --cream: #f3ede6;
    --page: #ffffff;
    --art-light: #e8f1f8;
    --art-mid: #cadeef;
  }
  * { margin: 0; padding: 0; box-sizing: border-box; }
  html, body { width: 1200px; height: 1200px; overflow: hidden; background: var(--page); }
  .cover {
    position: absolute; left: 55px; top: 210px; width: 1090px; height: 779px;
    background: var(--cover-blue);
  }
  /* Back cover */
  .back { position: absolute; left: 0; top: 0; width: 519px; height: 100%; }
  .back-title {
    position: absolute; left: 33px; top: 28px; width: 454px;
    font-family: 'Bebas Neue', sans-serif; font-size: 52px; line-height: 1;
    color: var(--white); white-space: nowrap; letter-spacing: 0.2px;
  }
  .blurb {
    position: absolute; left: 33px; top: 88px; width: 454px;
    font-family: 'Montserrat', sans-serif; font-size: 11.6px; line-height: 16.8px;
    color: var(--navy); text-align: justify;
  }
  .blurb p + p { margin-top: 17px; }
  .author-block {
    position: absolute; left: 33px; top: 402px; width: 454px;
    font-family: 'Montserrat', sans-serif; font-size: 11.6px; line-height: 16.8px;
    color: var(--navy); text-align: justify;
  }
  .author-photo {
    float: left; width: 116px; height: 122px; background: var(--white);
    margin: 0 10px 2px 0;
  }
  .author-heading {
    font-family: 'Bebas Neue', sans-serif; font-size: 30px; line-height: 28px;
    color: var(--white); text-align: left; letter-spacing: 0.5px;
  }
  .publisher {
    position: absolute; left: 33px; top: 654px;
    display: flex; align-items: center; gap: 10px;
    font-family: 'Montserrat', sans-serif; font-size: 13px; color: var(--navy);
  }
  .publisher-dot { width: 87px; height: 87px; border-radius: 50%; background: var(--white); }
  .barcode-area {
    position: absolute; left: 307px; top: 665px; width: 180px; height: 90px;
    background: var(--white);
  }
  /* Spine */
  .spine {
    position: absolute; left: 519px; top: 0; width: 52px; height: 100%;
    background: var(--white);
  }
  .spine-title, .spine-author {
    position: absolute; left: 50%; white-space: nowrap; color: var(--navy);
    transform-origin: left top; transform: rotate(90deg) translateY(-50%);
  }
  .spine-title {
    top: 35px; font-family: 'Oswald', sans-serif; font-weight: 700;
    font-size: 40px; line-height: 1; letter-spacing: -0.5px;
  }
  .spine-author {
    top: 597px; font-family: 'Bebas Neue', sans-serif; font-size: 32px;
    line-height: 1; letter-spacing: 1.5px;
  }
  /* Front cover */
  .front { position: absolute; left: 571px; top: 0; width: 519px; height: 100%; text-align: center; }
  .title-top {
    position: absolute; left: 0; width: 100%; top: 20px;
    font-family: 'Oswald', sans-serif; font-weight: 400; font-size: 84px;
    line-height: 1; color: var(--white); letter-spacing: -1px;
  }
  .title-to {
    position: absolute; left: 0; width: 100%; top: 100px;
    font-family: 'Oswald', sans-serif; font-weight: 400; font-size: 54px;
    line-height: 1; color: var(--white);
  }
  .title-main {
    position: absolute; left: 0; width: 100%; top: 148px;
    font-family: 'Oswald', sans-serif; font-weight: 700; font-size: 98px;
    line-height: 1; color: var(--navy); letter-spacing: -1px;
  }
  .subtitle {
    position: absolute; left: 0; width: 100%; top: 256px;
    font-family: 'Jost', sans-serif; font-size: 21.5px; line-height: 32.5px;
    color: var(--white);
  }
  .cover-art {
    position: absolute; left: 107px; top: 405px; width: 338px; height: 239px;
    background: linear-gradient(160deg, var(--art-light), var(--art-mid));
    border-radius: 4px;
  }
  .front-author {
    position: absolute; left: 0; width: 100%; top: 690px;
    font-family: 'Bebas Neue', sans-serif; font-size: 68px; line-height: 1;
    color: var(--cream); letter-spacing: 1px;
  }
</style>
</head>
<body>
<div class="cover">
  <section class="back">
    <h2 class="back-title">RETURNING TO STILLNESS</h2>
    <div class="blurb">
      <p>Returning to Stillness offers an evidence-based, step-by-step journey through a year of personal change. Drawing on his path of overcoming dyslexia, autism, trauma, and anxiety, Dr. Martin Olund blends mindfulness, psychology, and holistic healing in this accessible guide to lasting personal transformation.</p>
      <p>Unlike short-term programs, this book offers a full year of structured, practical exercises—scientifically grounded and deeply personal—to help you turn mindfulness into a lifelong habit. Each week, you'll explore simple yet profound practices to manage stress, build emotional resilience, and reconnect with your deeper wisdom. Through guided meditations, reflections, and trainings, you’ll rewire old patterns and learn to embrace the present moment with clarity and compassion. Whether you're seeking relief from chronic stress, clarity in uncertain times, or a deeper connection to yourself and your life, Gentle Renewal will meet you where you are. It’s not about perfection—it’s about learning to show up, fully present, for the beauty and messiness of life.</p>
    </div>
    <div class="author-block">
      <div class="author-photo" role="img" aria-label="Author photo placeholder"></div>
      <h3 class="author-heading">MARTIN OLUND</h3>
      <p>Martin Olund is a mindfulness and Dharma teacher, award-winning author, and former professor of social work with over 40 years of contemplative practice. He teaches insight meditation and has worked extensively with diverse communities, including unhoused populations, combat veterans with PTSD, and First Nations groups, blending mindfulness with deep cultural respect. Martin holds a PhD in social work and has authored several mindfulness and social justice books. He teaches with Quiet Harbor Sangha (QHS) and founded the Cedarline Stillness Sitting Circle. His teaching invites a return to presence, clarity, and compassionate action.</p>
    </div>
    <div class="publisher">
      <div class="publisher-dot"></div>
      <span class="publisher-name">Stillwater Press</span>
    </div>
    <div class="barcode-area"></div>
  </section>

  <section class="spine">
    <div class="spine-title">RETURNING TO STILLNESS</div>
    <div class="spine-author">MARTIN OLUND</div>
  </section>

  <section class="front">
    <h1>
      <span class="title-top">RETURNING</span>
      <span class="title-to">TO</span>
      <span class="title-main">STILLNESS</span>
    </h1>
    <p class="subtitle">Refreshing Your Routine to Ease Worry,<br>Grow Inner Awareness,<br>and Open Your Boundless Promise</p>
    <div class="cover-art" role="img" aria-label="Illustration of a desk calendar page labelled practice, marked with a large cross"></div>
    <div class="front-author">MARTIN OLUND</div>
  </section>
</div>
</body>
</html>
```